Adwords Banner for unique handmade Jewelery

We need one Banner for our Jewelerys
in 4 sizes:
300x250px
336x280px
728x90px
160x600px

http://www.torvik-mela.de/schmuck/2/

```html
<!DOCTYPE html>
<html lang="en">
<head>
<meta charset="utf-8">
<title>torvik &amp; mela – Jewellery Banners</title>
<link rel="stylesheet" href="https://fonts.googleapis.com/css2?family=Open+Sans:wght@400;600;700&display=swap">
<style>
  :root {
    --canvas: #ffffff;
    --banner-top: #f6d9e7;
    --banner-bottom: #fdf0f6;
    --banner-edge: #f3c8dc;
    --frame: #f5b6d3;
    --photo-light: #f4fbfb;
    --photo-teal: #7cc9c6;
    --photo-rose: #c5557f;
    --headline: #8c1b2e;
    --brand: #a9577a;
    --button: #000000;
    --button-text: #ffffff;
    --bloom: #f7c3dc;
  }
  * { box-sizing: border-box; margin: 0; padding: 0; }
  html, body { width: 1200px; height: 1042px; overflow: hidden; background: var(--canvas); }
  body { position: relative; font-family: "Open Sans", Arial, sans-serif; }

  .banner {
    position: absolute;
    overflow: hidden;
    border: 1px solid var(--banner-edge);
    background: linear-gradient(160deg, var(--banner-top) 0%, var(--banner-bottom) 55%, var(--banner-top) 100%);
  }
  .banner--leaderboard { left: 145px; top: 98px;  width: 853px; height: 105px; }
  .banner--skyscraper  { left: 145px; top: 241px; width: 187px; height: 701px; }
  .banner--large       { left: 372px; top: 241px; width: 393px; height: 326px; }
  .banner--medium      { left: 370px; top: 606px; width: 351px; height: 293px; }

  .bloom {
    position: absolute; right: -30px; bottom: -30px;
    width: 150px; height: 150px; border-radius: 50%;
    background: radial-gradient(circle, var(--bloom) 0%, rgba(247,195,220,0.4) 45%, rgba(247,195,220,0) 70%);
  }

  .brand {
    position: absolute;
    color: var(--brand);
    font-weight: 400;
    white-space: nowrap;
    letter-spacing: -0.5px;
  }

  .product {
    position: absolute;
    border: 3px solid var(--frame);
    background: #fff;
    padding: 4px;
  }
  .product__photo { width: 100%; height: 100%; }
  .product__photo--ring     { background: radial-gradient(circle at 45% 50%, var(--photo-teal) 0%, #b9dedd 38%, var(--photo-light) 62%); }
  .product__photo--earrings { background: radial-gradient(ellipse at 50% 55%, var(--photo-rose) 0%, #e3a6bf 35%, var(--photo-light) 65%); }
  .product__photo--necklace { background: linear-gradient(180deg, var(--photo-light) 0%, var(--photo-light) 40%, #a8dcd9 70%, #f0c2d3 100%); }

  .headline {
    position: absolute;
    color: var(--headline);
    text-align: center;
    line-height: 1.3;
    text-transform: uppercase;
  }
  .headline__lead { display: block; font-weight: 400; white-space: nowrap; }
  .headline__key  { display: block; font-weight: 700; letter-spacing: 0.8px; white-space: nowrap; }

  .cta {
    position: absolute;
    background: var(--button);
    color: var(--button-text);
    font-weight: 600;
    letter-spacing: 0.8px;
    text-transform: uppercase;
    display: flex; align-items: center; justify-content: center;
    text-decoration: none;
  }
</style>
</head>
<body>

  <!-- 728 x 90 -->
  <section class="banner banner--leaderboard" aria-label="Leaderboard banner">
    <div class="bloom" role="img" aria-label="Soft pink flower decoration"></div>
    <span class="brand" style="left:20px; top:33px; font-size:28px;">torvik &amp; mela</span>
    <div class="product" style="left:241px; top:9px; width:107px; height:89px;"><div class="product__photo product__photo--ring" role="img" aria-label="Silver ring with turquoise glass stone"></div></div>
    <div class="product" style="left:354px; top:9px; width:107px; height:89px;"><div class="product__photo product__photo--earrings" role="img" aria-label="Pink and turquoise glass drop earring"></div></div>
    <div class="product" style="left:467px; top:9px; width:107px; height:89px;"><div class="product__photo product__photo--necklace" role="img" aria-label="Silver chain with turquoise and pink glass hearts"></div></div>
    <p class="headline" style="left:578px; top:15px; width:270px; font-size:14px; line-height:1.25;">
      <span class="headline__lead">Our extensive range of beautiful</span>
      <span class="headline__key">Eye catching jewellery</span>
    </p>
    <a class="cta" href="http://www.torvik-mela.de/schmuck/2/" style="left:655px; top:60px; width:114px; height:33px; font-size:13px;">Shop now</a>
  </section>

  <!-- 160 x 600 -->
  <section class="banner banner--skyscraper" aria-label="Skyscraper banner">
    <div class="bloom" role="img" aria-label="Soft pink flower decoration" style="width:190px; height:190px; bottom:60px;"></div>
    <span class="brand" style="left:0; width:100%; text-align:center; top:32px; font-size:23px;">torvik &amp; mela</span>
    <div class="product" style="left:22px; top:122px; width:142px; height:100px;"><div class="product__photo product__photo--necklace" role="img" aria-label="Silver chain with turquoise and pink glass hearts"></div></div>
    <div class="product" style="left:22px; top:232px; width:142px; height:100px;"><div class="product__photo product__photo--earrings" role="img" aria-label="Pink and turquoise glass drop earring"></div></div>
    <div class="product" style="left:22px; top:343px; width:142px; height:100px;"><div class="product__photo product__photo--ring" role="img" aria-label="Silver ring with turquoise glass stone"></div></div>
    <p class="headline" style="left:0; top:487px; width:100%; font-size:15px; line-height:1.4;">
      <span class="headline__lead">Our extensive<br>range of beautiful</span>
      <span class="headline__key" style="margin-top:10px;">Eye catching<br>jewellery</span>
    </p>
    <a class="cta" href="http://www.torvik-mela.de/schmuck/2/" style="left:36px; top:626px; width:114px; height:35px; font-size:13px;">Shop now</a>
  </section>

  <!-- 336 x 280 -->
  <section class="banner banner--large" aria-label="Large rectangle banner">
    <div class="bloom" role="img" aria-label="Soft pink flower decoration" style="width:190px; height:190px;"></div>
    <span class="brand" style="left:0; width:100%; text-align:center; top:26px; font-size:34px;">torvik &amp; mela</span>
    <div class="product" style="left:29px; top:105px; width:108px; height:89px;"><div class="product__photo product__photo--ring" role="img" aria-label="Silver ring with turquoise glass stone"></div></div>
    <div class="product" style="left:141px; top:105px; width:108px; height:89px;"><div class="product__photo product__photo--earrings" role="img" aria-label="Pink and turquoise glass drop earring"></div></div>
    <div class="product" style="left:254px; top:105px; width:108px; height:89px;"><div class="product__photo product__photo--necklace" role="img" aria-label="Silver chain with turquoise and pink glass hearts"></div></div>
    <p class="headline" style="left:0; top:214px; width:100%; font-size:15.5px;">
      <span class="headline__lead">Our extensive range of beautiful</span>
      <span class="headline__key">Eye catching jewellery</span>
    </p>
    <a class="cta" href="http://www.torvik-mela.de/schmuck/2/" style="left:134px; top:271px; width:113px; height:34px; font-size:13px;">Shop now</a>
  </section>

  <!-- 300 x 250 -->
  <section class="banner banner--medium" aria-label="Medium rectangle banner">
    <div class="bloom" role="img" aria-label="Soft pink flower decoration" style="width:180px; height:180px;"></div>
    <span class="brand" style="left:0; width:100%; text-align:center; top:22px; font-size:31px;">torvik &amp; mela</span>
    <div class="product" style="left:27px; top:95px; width:96px; height:89px;"><div class="product__photo product__photo--ring" role="img" aria-label="Silver ring with turquoise glass stone"></div></div>
    <div class="product" style="left:128px; top:95px; width:96px; height:89px;"><div class="product__photo product__photo--earrings" role="img" aria-label="Pink and turquoise glass drop earring"></div></div>
    <div class="product" style="left:229px; top:95px; width:96px; height:89px;"><div class="product__photo product__photo--necklace" role="img" aria-label="Silver chain with turquoise and pink glass hearts"></div></div>
    <p class="headline" style="left:0; top:200px; width:100%; font-size:14.5px; line-height:1.25;">
      <span class="headline__lead">Our extensive range of beautiful</span>
      <span class="headline__key">Eye catching jewellery</span>
    </p>
    <a class="cta" href="http://www.torvik-mela.de/schmuck/2/" style="left:121px; top:247px; width:101px; height:29px; font-size:12px;">Shop now</a>
  </section>

</body>
</html>
```